Hochzeitseinladung
Zielgruppe
Gastronomie - Zielgruppe ist ein Hochzeitspaar, welches bei uns feiert. Wir dürfen Ihre Hochzeitseinladung entwerfen.
Aufgabenstellung
Den Textvorschlag des Brautpaares findet Ihr im Anhang. Das Thema der Hochzeit ist AMORE.
1. Die Hochzeitseinladung darf gerne kreativ gestaltet sein, vielleicht in Form des Moodboard-Bildes im Anhang? Mattes hat braune Haare und Locken und Doreen lange braune Haare. Beide tragen eine Brille.
Das Hochzeitspaar hat noch einen kleinen braunen Zwergpudel 'Fips', vielleicht findet er auch noch Platz auf der Einladungskarte ;-).
2. Als Alternativ-Vorschlag wäre ein klassisches Design auf zB geprägtem Papier toll.
3. Etwas Schlichtes mit einem Neon-Accessoire würde das Hochzeitspaar auch gut finden. Zb brauner Karton mit einem Neonband.

```html
<!DOCTYPE html>
<html lang="de">
<head>
<meta charset="utf-8">
<title>Hochzeitseinladung Doreen und Mattes</title>
<link href="https://fonts.googleapis.com/css2?family=Montserrat:wght@400;500;600;700&family=Mrs+Saint+Delafield&display=swap" rel="stylesheet">
<style>
  :root {
    --backdrop: #d4b6a6;
    --card: #ffffff;
    --ink: #3a3a3a;
    --ink-strong: #111111;
    --rule: #555555;
    --poodle: #d6c3b5;
  }
  * { margin: 0; padding: 0; box-sizing: border-box; }
  html, body { width: 1200px; height: 1200px; overflow: hidden; }
  body {
    background: var(--backdrop);
    position: relative;
    font-family: "Montserrat", sans-serif;
    color: var(--ink);
  }
  .card {
    position: absolute;
    top: 138px;
    width: 432px;
    height: 924px;
    background: var(--card);
  }
  .card--invite { left: 137px; }
  .card--schedule { left: 627px; }

  .vertical-rule {
    position: absolute;
    width: 1px;
    background: var(--rule);
  }
  .card--invite .vertical-rule { left: 370px; top: 56px; height: 158px; }
  .card--schedule .vertical-rule { left: 375px; top: 58px; height: 157px; }

  .vertical-word {
    position: absolute;
    display: flex;
    flex-direction: column;
    align-items: center;
    font-size: 11px;
    font-weight: 400;
    line-height: 1;
    color: var(--ink);
    width: 20px;
  }
  .card--invite .vertical-word { left: 360px; top: 252px; gap: 7.6px; }
  .card--invite .vertical-word .gap { height: 11px; }
  .card--schedule .vertical-word { left: 365px; top: 239px; gap: 12.5px; font-size: 12px; }

  .couple {
    position: absolute;
    left: 57px;
    top: 318px;
  }
  .couple__name {
    font-size: 20px;
    font-weight: 600;
    letter-spacing: 0.33em;
    color: var(--ink);
    line-height: 1;
  }
  .couple__and {
    font-family: "Mrs Saint Delafield", cursive;
    font-size: 34px;
    line-height: 1;
    color: var(--ink);
    margin: 10px 0 6px 20px;
    height: 44px;
    position: relative;
  }
  .couple__and::before, .couple__and::after {
    content: "";
    position: absolute;
    top: 22px;
    height: 1px;
    background: var(--ink);
    width: 30px;
  }
  .couple__and::before { left: -25px; }
  .couple__and::after { left: 62px; width: 40px; }
  .couple__and span { position: relative; left: 8px; top: -2px; }

  .details {
    position: absolute;
    left: 57px;
    top: 452px;
    font-size: 9.5px;
    letter-spacing: 0.24em;
    line-height: 17px;
    color: var(--ink);
    font-variant: small-caps;
  }

  .poodle-illustration {
    position: absolute;
    left: 173px;
    top: 551px;
    width: 202px;
    height: 292px;
    border-radius: 46% 46% 30% 30% / 35% 35% 20% 20%;
    background: radial-gradient(ellipse at 45% 40%, #d9c6b8 0%, var(--poodle) 60%, #e3d4c9 100%);
  }

  .schedule {
    position: absolute;
    left: 62px;
    top: 242px;
    width: 330px;
  }
  .schedule__item { margin-bottom: 31px; }
  .schedule__time {
    font-size: 10px;
    font-weight: 700;
    letter-spacing: 0.32em;
    color: var(--ink-strong);
    line-height: 20px;
    font-variant: small-caps;
    text-transform: lowercase;
  }
  .schedule__time b { font-size: 11px; text-transform: none; }
  .schedule__line {
    font-size: 9.5px;
    font-weight: 400;
    letter-spacing: 0.3em;
    color: var(--ink-strong);
    line-height: 20px;
    font-variant: small-caps;
  }
  .schedule__ps { margin-top: 42px; }
</style>
</head>
<body>
  <section class="card card--invite">
    <div class="vertical-rule"></div>
    <div class="vertical-word" aria-label="Wir heiraten">
      <span>W</span><span>I</span><span>R</span><span class="gap"></span><span>H</span><span>E</span><span>I</span><span>R</span><span>A</span><span>T</span><span>E</span><span>N</span>
    </div>
    <div class="couple">
      <p class="couple__name">DOREEN</p>
      <p class="couple__and"><span>and</span></p>
      <p class="couple__name">MATTES</p>
    </div>
    <div class="details">
      <p>MÜNSTER</p>
      <p>Motto amore</p>
    </div>
    <div class="poodle-illustration" role="img" aria-label="Zeichnung des braunen Zwergpudels Fips mit Halsband"></div>
  </section>

  <section class="card card--schedule">
    <div class="vertical-rule"></div>
    <div class="vertical-word" aria-label="Ablauf">
      <span>A</span><span>B</span><span>A</span><span>U</span><span>F</span>
    </div>
    <div class="schedule">
      <div class="schedule__item">
        <p class="schedule__time"><b>13.30</b> Uhr Standesamt</p>
        <p class="schedule__line">LINDENHOF KLOSTER</p>
      </div>
      <div class="schedule__item">
        <p class="schedule__time"><b>13.45</b> Uhr Trauung</p>
      </div>
      <div class="schedule__item">
        <p class="schedule__time"><b>14.30</b> Uhr Sekt-Empfang</p>
        <p class="schedule__line">salon aurelia</p>
        <p class="schedule__line">Rosengasse 4</p>
      </div>
      <div class="schedule__item">
        <p class="schedule__time"><b>16</b> Uhr Pause</p>
      </div>
      <div class="schedule__item">
        <p class="schedule__time"><b>18.30</b> Uhr Empfang Gasthaus</p>
        <p class="schedule__line">goldener anker</p>
        <p class="schedule__line">kornmarkt 45</p>
      </div>
      <div class="schedule__item">
        <p class="schedule__time">Flying Dinner</p>
        <p class="schedule__line">cocktails und party</p>
      </div>
      <div class="schedule__item">
        <p class="schedule__time">Dresscodes</p>
        <p class="schedule__line">day Cocktail</p>
        <p class="schedule__line">night Black Tie</p>
      </div>
      <p class="schedule__line schedule__ps">ps don’t forget your dancing shoes</p>
    </div>
  </section>
</body>
</html>
```